Letterhead for SaaS

Design a letterhead that aligns with our new business card, using our logo and color scheme and text defined in the Branding Guide to ensure consistency. Consider incorporating a subtle watermark for added elegance. The layout should reflect the card's style, creating a cohesive look across our stationery.

```html
<!DOCTYPE html>
<html lang="en">
<head>
<meta charset="utf-8">
<title>Valcrest Letterhead</title>
<link href="https://fonts.googleapis.com/css2?family=Montserrat:wght@400;600&family=Lato:wght@400&family=Open+Sans:wght@600&family=Kanit:wght@700&family=Mrs+Saint+Delafield&display=swap" rel="stylesheet">
<style>
  :root {
    --navy: #131a2b;
    --navy-light: #1f2b47;
    --accent: #14b4ee;
    --ink: #161c2a;
    --body: #6b6e74;
    --meta: #4a4d52;
    --bg: #e8e9eb;
    --paper: #ffffff;
    --watermark: #eff0f1;
  }
  * { margin: 0; padding: 0; box-sizing: border-box; }
  html, body { width: 999px; height: 1200px; overflow: hidden; background: var(--bg); }
  .letterhead {
    position: absolute; left: 72px; top: 0;
    width: 855px; height: 1200px;
    background: var(--paper); overflow: hidden;
  }
  .header-band {
    position: absolute; left: 207px; top: 66px; width: 648px; height: 140px;
    background: linear-gradient(120deg, var(--navy) 0%, var(--navy-light) 45%, var(--navy) 70%, #18223a 100%);
  }
  .brand {
    position: absolute; left: 226px; top: 154px;
    display: flex; align-items: center; gap: 12px;
  }
  .brand-dot { width: 20px; height: 20px; border-radius: 50%; background: var(--accent); }
  .brand-name {
    font-family: 'Kanit', sans-serif; font-weight: 700; font-size: 36px;
    color: #ffffff; letter-spacing: 0.5px; line-height: 1;
  }
  .company-address {
    position: absolute; right: 77px; top: 110px; text-align: right;
    font-family: 'Lato', sans-serif; font-style: normal; font-size: 14px; line-height: 21px; color: #ffffff;
  }
  .recipient { position: absolute; left: 77px; top: 346px; }
  .recipient-name {
    font-family: 'Montserrat', sans-serif; font-weight: 600; font-size: 26px; color: var(--ink);
    margin-bottom: 14px;
  }
  .recipient-detail {
    font-family: 'Montserrat', sans-serif; font-size: 14px; color: var(--meta); line-height: 19px;
  }
  .recipient-detail.gap { margin-bottom: 7px; }
  .letter-date {
    position: absolute; right: 77px; top: 474px;
    font-family: 'Open Sans', sans-serif; font-weight: 600; font-size: 18px; color: var(--meta);
  }
  .letter-body { position: absolute; left: 78px; top: 520px; width: 700px; }
  .letter-body p {
    font-family: 'Montserrat', sans-serif; font-size: 15.6px; line-height: 25.2px;
    color: var(--body); text-align: justify; margin-bottom: 25px;
  }
  .watermark {
    position: absolute; left: 60px; top: 1040px; width: 250px; height: 250px;
    border-radius: 50%; background: var(--watermark);
  }
  .sign-off { position: absolute; right: 83px; top: 850px; text-align: right; }
  .sign-off-name { font-family: 'Lato', sans-serif; font-size: 21px; color: var(--ink); }
  .signature {
    font-family: 'Mrs Saint Delafield', cursive; font-size: 40px; color: var(--ink);
    margin-top: 10px; margin-right: 8px;
  }
  .footer-band {
    position: absolute; left: 221px; top: 1120px; width: 634px; height: 35px;
    background: var(--navy);
    display: flex; align-items: center; padding-left: 70px; gap: 14px;
  }
  .contact-item {
    display: flex; align-items: center; gap: 6px;
    font-family: 'Lato', sans-serif; font-size: 13.5px; color: #ffffff;
  }
  .contact-icon {
    width: 17px; height: 17px; border-radius: 2px; background: var(--accent);
    display: flex; align-items: center; justify-content: center;
  }
</style>
</head>
<body>
  <main class="letterhead">
    <div class="header-band" role="img" aria-label="Dark navy band with faint faceted geometric shading"></div>
    <div class="brand">
      <span class="brand-dot"></span>
      <span class="brand-name">VALCREST</span>
    </div>
    <address class="company-address">7310 Lakeview<br>Avenue Midtown<br>DC 20019</address>

    <section class="recipient">
      <h1 class="recipient-name">Mr. Aaron Kettle</h1>
      <p class="recipient-detail gap">0147-258-369</p>
      <p class="recipient-detail gap">hello@valcrestmail.com</p>
      <p class="recipient-detail">5821 Harbor Crest Rd. Suite</p>
      <p class="recipient-detail">210 Dallas, TX 0000</p>
    </section>

    <p class="letter-date">12 December, 2024</p>

    <section class="letter-body">
      <p>Lorem ipsum dolor sit amet, consectetuer adipiscing elit, sed diam nonummy nibh euismod tincidunt ut laoreet dolore magna aliquam erat volutpat. Ut wisi enim ad minim veniam, quis nostrud exerci tation ullamcorper suscipit lobortis nisl ut aliquip ex ea commodo consequat. Duis autem vel eum iriure dolor in hendrerit in vulputate velit esse molestie consequat, vel illum dolore eu feugiat nulla facilisis at vero eros et accumsan et iusto odio dignissim qui blandit praesent luptatum zzril delenit augue duis dolore te feugait nulla facilisi.</p>
      <p>Lorem ipsum dolor sit amet, cons ectetuer adipiscing elit, sed diam nonummy nibh euismod tincidunt ut laoreet dolore magna aliquam erat volutpat. Ut wisi enim ad minim veniam, quis nostrud exerci tation ullamcorper suscipit lobortis nisl ut aliquip ex ea commodo consequat.</p>
    </section>

    <div class="watermark" aria-hidden="true"></div>

    <section class="sign-off">
      <p class="sign-off-name">Mr. Aaron Kettle</p>
      <p class="signature">Aaron Kettle</p>
    </section>

    <footer class="footer-band">
      <span class="contact-item">
        <span class="contact-icon">
          <svg width="11" height="11" viewBox="0 0 24 24"><path fill="#fff" d="M6.6 10.8a15.1 15.1 0 0 0 6.6 6.6l2.2-2.2a1 1 0 0 1 1-.25 11.4 11.4 0 0 0 3.6.57 1 1 0 0 1 1 1V20a1 1 0 0 1-1 1A17 17 0 0 1 3 4a1 1 0 0 1 1-1h3.5a1 1 0 0 1 1 1c0 1.25.2 2.45.57 3.57a1 1 0 0 1-.25 1z"/></svg>
        </span>+00 987 654 32
      </span>
      <span class="contact-item">
        <span class="contact-icon">
          <svg width="11" height="9" viewBox="0 0 22 16"><rect x="1" y="1" width="20" height="14" fill="none" stroke="#fff" stroke-width="2"/><path d="M1 1l10 8 10-8" fill="none" stroke="#fff" stroke-width="2"/></svg>
        </span>team@valcrestmail.com
      </span>
      <span class="contact-item">
        <span class="contact-icon">
          <svg width="10" height="11" viewBox="0 0 20 22"><path fill="#fff" d="M3 1l14 10-6 1 4 8-3 1.5-4-8-5 4z"/></svg>
        </span>www.valcrestapp.com
      </span>
    </footer>
  </main>
</body>
</html>
```